Bright Oak Fitness Facility Business Cards

Business Card Design that incorporates the logo and tagline

Target Market(s)

Fitness, People Who Exercise

Contact Information for Business Card

2817 Mossgrove Bend Road
Marlow Springs, Oregon 97190
Phone: 541-555-Jump (5867)
www.brightoakfitness.example
info@brightoakfitness.example

Requirements
Must have
• Logo, Address, Website, email and tagline "Stronger Every Day". Colors should be red/black/grey/white

```html
<!DOCTYPE html>
<html lang="en">
<head>
<meta charset="utf-8">
<title>Bright Oak Fitness – Business Cards</title>
<link rel="stylesheet" href="https://fonts.googleapis.com/css2?family=Arimo:wght@400;700&display=swap">
<style>
  :root {
    --bg: #e2e2e2;
    --card-light: #e4e4e4;
    --card-dark: #121212;
    --red: #d9252a;
    --ink: #1a1a1a;
    --grey: #6b6b6b;
    --rule: #7a7a7a;
    --white: #f1f1f1;
  }
  * { margin: 0; padding: 0; box-sizing: border-box; }
  html, body { width: 1200px; height: 1200px; overflow: hidden; }
  body {
    background: var(--bg);
    font-family: "Arimo", Arial, sans-serif;
    position: relative;
  }
  .card {
    position: absolute;
    left: 227px;
    width: 745px;
    height: 425px;
  }
  .card--front { top: 135px; background: var(--card-light); }
  .card--back  { top: 639px; background: var(--card-dark); }

  .brand {
    position: absolute;
    display: flex;
    align-items: center;
    gap: 12px;
    font-weight: 700;
    white-space: nowrap;
    line-height: 1;
  }
  .brand__mark { width: 28px; height: 28px; background: var(--red); flex: none; }
  .brand__name { color: var(--red); font-size: 40px; letter-spacing: 0.3px; }

  .card--front .brand { left: 34px; top: 124px; }
  .card--back .brand {
    left: 0; right: 0; top: 226px;
    justify-content: center;
  }
  .card--back .brand__name { color: var(--white); font-size: 44px; }

  .person { position: absolute; left: 34px; top: 243px; }
  .person__name { color: var(--red); font-size: 27px; font-weight: 400; line-height: 1; letter-spacing: 0.2px; }
  .person__title { color: var(--grey); font-size: 17px; margin-top: 9px; line-height: 1; }

  .divider {
    position: absolute; left: 0; right: 0; top: 307px;
    height: 1px; background: var(--rule);
  }
  .divider__accent {
    position: absolute; left: 34px; top: -1px;
    width: 203px; height: 2px; background: var(--red);
  }

  .contacts {
    position: absolute; left: 34px; top: 325px;
    list-style: none;
    color: var(--grey); font-size: 17px;
  }
  .contacts li { display: flex; align-items: center; gap: 7px; height: 23.5px; }
  .contacts svg { width: 15px; height: 15px; fill: var(--red); flex: none; }

  .address {
    position: absolute; right: 34px; top: 349px;
    text-align: right;
    color: var(--grey); font-size: 17px; line-height: 24px;
    font-style: normal;
  }

  .tagline {
    position: absolute; left: 0; right: 0; top: 376px;
    text-align: center;
    color: var(--red); font-size: 18px; line-height: 1; letter-spacing: 0.2px;
  }
</style>
</head>
<body>
  <section class="card card--front">
    <div class="brand">
      <span class="brand__mark"></span>
      <span class="brand__name">BRIGHT OAK FITNESS</span>
    </div>

    <div class="person">
      <h1 class="person__name">MARCUS DELANEY</h1>
      <p class="person__title">Managing Director</p>
    </div>

    <div class="divider"><span class="divider__accent"></span></div>

    <ul class="contacts">
      <li>
        <svg viewBox="0 0 16 16" aria-hidden="true"><path d="M1 6c0-2 3-3.5 7-3.5S15 4 15 6v1h-3.5V5.5h-7V7H1zM4 8h8l2 6H2z"/></svg>
        541-555-Jump (5867)
      </li>
      <li>
        <svg viewBox="0 0 16 16" aria-hidden="true"><path d="M1 3h14v10H1zM2.5 4.5v.4L8 9l5.5-4.1v-.4zM2.5 6.7v4.8h11V6.7L8 10.8z"/></svg>
        info@brightoakfitness.example
      </li>
      <li>
        <svg viewBox="0 0 16 16" aria-hidden="true"><circle cx="8" cy="8" r="7"/></svg>
        www.brightoakfitness.example
      </li>
    </ul>

    <address class="address">
      2817 Mossgrove Bend Road<br>
      Marlow Springs, Oregon 97190
    </address>
  </section>

  <section class="card card--back">
    <div class="brand">
      <span class="brand__mark"></span>
      <span class="brand__name">BRIGHT OAK FITNESS</span>
    </div>
    <p class="tagline">STRONGER EVERY DAY</p>
  </section>
</body>
</html>
```